Kalvendor Whitmane & Associates

We would like a simple, professional business card using a similar font to our logo.

Industry/Entity Type

Law Firm

Contact Information for Business Card

Martin Kalvendor, Esq. 48 Fennimore Lane, 2nd Floor Brenholt, NR 04173 Office: 555.216.4093 Cell: 555.370.8154 Email: marty@kwlawfirm.example kalvendorwhitmanelaw.example

Font styles to use
Other font styles liked:
• We would like to use the fonts used in the logo or similar

Colors
0054AA
0677BA
7BADD7
CADEEF
E8F1F8

Requirements
Must have
• We would like the fonts to match the logo
Nice to have
• not too much design- very simple and professional business card. I added a picture of a business card that I tried to start but I am not a designer! Hopefully it will help with the address and phone numbers and kind of what we are looking for.

```html
<!DOCTYPE html>
<html lang="en">
<head>
<meta charset="utf-8">
<title>Kalvendor Whitmane &amp; Associates — Business Card</title>
<link rel="stylesheet" href="https://fonts.googleapis.com/css2?family=Arimo:wght@400;700&family=Cinzel:wght@600&display=swap">
<style>
  :root {
    --navy: #1f3670;
    --ink-grey: #666a70;
    --rule-grey: #8a8d92;
    --paper: #ffffff;
    --backdrop: #e6e6e6;
    --wash: #eef0f5;
    --edge-grey: #6e6f72;
  }
  * { margin: 0; padding: 0; box-sizing: border-box; }
  html, body { width: 1200px; height: 801px; overflow: hidden; }
  body {
    background: var(--backdrop);
    font-family: "Arimo", Arial, sans-serif;
    position: relative;
  }
  .card {
    position: absolute;
    top: 240px;
    width: 525px;
    height: 300px;
    box-shadow: 0 6px 18px rgba(0,0,0,0.18);
    overflow: hidden;
  }
  .card--front { left: 50px; background: var(--paper); }
  .card--back { left: 625px; background: var(--navy); }

  .front__wash {
    position: absolute; right: 6px; top: 0;
    width: 220px; height: 286px;
    background: var(--wash);
  }
  .front__edge {
    position: absolute; right: 0; top: 0;
    width: 6px; height: 286px;
    background: var(--edge-grey);
  }
  .front__band {
    position: absolute; left: 270px; right: 0; bottom: 0;
    height: 14px; background: var(--navy);
  }
  .front__name {
    position: absolute; right: 30px; top: 26px;
    font-weight: 700; font-size: 17px; color: var(--navy);
  }

  .brand { position: absolute; display: flex; align-items: center; gap: 12px; }
  .brand__square { width: 40px; height: 40px; flex: none; }
  .brand__rule { width: 1px; align-self: stretch; flex: none; }
  .brand__name {
    font-family: "Cinzel", Georgia, serif;
    font-weight: 600; font-size: 15px; line-height: 1.1;
    letter-spacing: 0.04em; text-transform: uppercase;
  }
  .card--front .brand { left: 30px; top: 62px; }
  .card--front .brand__square { background: var(--navy); }
  .card--front .brand__rule { background: var(--rule-grey); }
  .card--front .brand__name { color: var(--navy); }

  .card--back .brand { left: 50%; top: 50%; transform: translate(-50%, -50%); gap: 16px; }
  .card--back .brand__square { background: var(--paper); width: 56px; height: 48px; }
  .card--back .brand__rule { background: var(--paper); }
  .card--back .brand__name { color: var(--paper); font-size: 20px; }

  .address {
    position: absolute; left: 30px; top: 132px;
    color: var(--ink-grey); font-size: 12.5px; line-height: 1.35;
  }
  .contacts {
    position: absolute; left: 30px; top: 192px;
    list-style: none; color: var(--ink-grey); font-size: 12.5px; line-height: 1.4;
  }
  .contacts li { display: flex; align-items: center; gap: 7px; }
  .contacts svg { width: 10px; height: 10px; fill: var(--navy); flex: none; }
</style>
</head>
<body>
  <section class="card card--front" aria-label="Business card front">
    <div class="front__wash"></div>
    <div class="front__edge"></div>
    <div class="front__band"></div>
    <p class="front__name">Martin Kalvendor, Esq.</p>
    <div class="brand">
      <span class="brand__square"></span>
      <span class="brand__rule"></span>
      <p class="brand__name">Kalvendor<br>Whitmane<br>&amp; Associates</p>
    </div>
    <p class="address">48 Fennimore Lane<br>2nd Floor Brenholt<br>NR 04173</p>
    <ul class="contacts">
      <li><svg viewBox="0 0 10 10"><path d="M2 0.5 L4 2.8 L3 4 Q4.5 6 6 7 L7.2 6 L9.5 8 L8 9.5 Q3.5 9 0.5 2 Z"/></svg>555.216.4093</li>
      <li><svg viewBox="0 0 10 10"><path d="M2.5 0 H7.5 V10 H2.5 Z M3.3 1 V8.3 H6.7 V1 Z"/></svg>555.370.8154</li>
      <li><svg viewBox="0 0 10 10"><path d="M0 2 H10 V8.5 H0 Z M0.8 2.6 L5 5.6 L9.2 2.6 Z"/></svg>marty@kwlawfirm.example</li>
      <li><svg viewBox="0 0 10 10"><circle cx="5" cy="5" r="4.8"/></svg>www.kalvendorwhitmanelaw.example</li>
    </ul>
  </section>

  <section class="card card--back" aria-label="Business card back">
    <div class="brand">
      <span class="brand__square"></span>
      <span class="brand__rule"></span>
      <p class="brand__name">Kalvendor<br>Whitmane<br>&amp; Associates</p>
    </div>
  </section>
</body>
</html>
```